New Architectural Firm Business Cards

New Business card to compliment previous pixel forum logo (attached). Please design a business card that is simple, modern, creative....please do not use "symbols", simply the logo and associated graphics/text. The front should contain name/address/phone/email/web address (with graphics).....back should be 100% graphic design using the logo somehow. Hoping for a two color (black and yellow) design. full bleed design, no borders

Target Market(s)

Commercial Architecture Clients

Industry/Entity Type

Architecture

Contact Information for Business Card

Please design a business card that is simple, modern, creative....please do not use "symbols", simply the logo and associated graphics/text. The front should contain name/address/phone/email/web address (with graphics).....back should be 100% graphic design using the logo somehow

Font styles to use
Sans Serif

Colors
FFF300
FFF600
FEFA6F
FFFEC7
FFFEE8

Requirements
Must have
• Clean, Modern Design
Should not have
• Stock images or "icons"

```html
<!DOCTYPE html>
<html lang="en">
<head>
<meta charset="utf-8">
<title>Kestrel Architecture – Business Cards</title>
<link href="https://fonts.googleapis.com/css2?family=Roboto+Condensed:wght@400;500;700&display=swap" rel="stylesheet">
<style>
  :root {
    --backdrop: #cbcbcb;
    --brand-yellow: #f5c400;
    --brand-black: #000000;
    --card-radius: 24px;
  }
  html, body {
    margin: 0;
    padding: 0;
    width: 1200px;
    height: 848px;
    overflow: hidden;
    background: var(--backdrop);
    font-family: "Roboto Condensed", Arial, sans-serif;
  }
  .canvas {
    position: relative;
    width: 1200px;
    height: 848px;
  }
  .card {
    position: absolute;
    top: 245px;
    width: 205px;
    height: 359px;
    border-radius: var(--card-radius);
    box-sizing: border-box;
    text-align: center;
  }
  .card--front {
    left: 372px;
    background: var(--brand-yellow);
    color: var(--brand-black);
  }
  .card--back {
    left: 623px;
    background: var(--brand-black);
    color: var(--brand-yellow);
  }
  .wordmark {
    position: absolute;
    left: 0;
    right: 0;
    font-weight: 500;
    line-height: 1;
    text-transform: uppercase;
  }
  .wordmark__name {
    display: block;
    font-size: 46px;
    letter-spacing: 0.5px;
  }
  .wordmark__type {
    display: block;
    font-size: 25px;
    margin-top: 8px;
    letter-spacing: 0.3px;
  }
  .card--front .wordmark { top: 340px; }
  .card--front .wordmark { top: 92px; }
  .card--back .wordmark { top: 250px; }
  .contact {
    position: absolute;
    left: 0;
    right: 0;
    top: 196px;
    font-size: 11.5px;
    line-height: 15.5px;
  }
  .contact__person {
    font-weight: 700;
    font-size: 16px;
    margin: 0 0 10px;
  }
  .contact__lines {
    margin: 0 0 8px;
  }
  .contact__label { font-weight: 700; }
  .contact__web {
    font-weight: 700;
    margin: 0 0 9px;
  }
  .contact__address {
    margin: 0;
    font-style: normal;
  }
</style>
</head>
<body>
  <main class="canvas">
    <section class="card card--front" aria-label="Business card front">
      <div class="wordmark">
        <span class="wordmark__name">Kestrel</span>
        <span class="wordmark__type">Architecture</span>
      </div>
      <div class="contact">
        <p class="contact__person">Name Lastname</p>
        <p class="contact__lines">
          <span class="contact__label">phone:</span> +44 (0) 20 7946 0321<br>
          <span class="contact__label">email:</span> studio@kestrelarch.com
        </p>
        <p class="contact__web">www.kestrelarch.com</p>
        <address class="contact__address">
          Unit 12 Harbour Yard<br>
          8 Calder Lane, London<br>
          United Kingdom, N7 4QT
        </address>
      </div>
    </section>

    <section class="card card--back" aria-label="Business card back">
      <div class="wordmark">
        <span class="wordmark__name">Kestrel</span>
        <span class="wordmark__type">Architecture</span>
      </div>
    </section>
  </main>
</body>
</html>
```